Door Hanger General Contractor

design high quality marketing piece to promote our general contractor business.
Use all content create badges, banners, bubbles, boxes ect to highlight text.
Template format is uploaded in images
Make font as large as possible, minimize negative space, fill areas
FRONT SIDE
Your Neighbor Just Remodeled
Come See Our Work at:
(under this create blank white box placeholder for address)
LOVE YOUR HOME AGAIN!
WE MAKE REMODELING EASY
FREE 3D DESIGN SERVICES
FREE ESTIMATES
LICENSED GENERAL CONTRACTORS
We Specialize in:
Kitchen Remodel
Bathroom Remodel
Interior/Exterior Painting
Flooring: Carpet, Vinyl, Wood & Tile
Energy Efficient Upgrades
Window/Door Replacement
WATER & MOLD DAMAGE
BACK SIDE
GET STARTED IN 3 SIMPLE STEPS:
1 ORDER FREE ESTIMATE & DESIGN
2 APPROVE ESTIMATE & DESIGN
3 HEARTHWELL BUILDERS BUILDS YOUR DREAM
Thinking About Selling?
We Buy Homes
GET CASH OFFER
SELLING MADE EASY
CALL NOW!!
Hearthwell Builders Inc.
858-555-0147 Call/Text
OakvaleHomeworks.example
CSLB# 4820516
home owners
General Contractor

```html
<!DOCTYPE html>
<html lang="en">
<head>
<meta charset="utf-8">
<title>Hearthwell Builders – Door Hangers</title>
<link rel="stylesheet" href="https://fonts.googleapis.com/css2?family=Bebas+Neue&family=Tinos:wght@400;700&display=swap">
<style>
  :root{
    --stage:#767676;
    --blue:#4489ef;
    --ink:#141414;
    --white:#ffffff;
  }
  *{box-sizing:border-box;margin:0;padding:0}
  html,body{width:1081px;height:1200px;overflow:hidden;background:var(--stage)}
  .stage{position:relative;width:1081px;height:1200px}
  .hanger{position:absolute;top:74px;width:409px;height:1057px;background:var(--blue);overflow:hidden;box-shadow:0 4px 14px rgba(0,0,0,.35);font-family:"Tinos",serif;color:var(--white)}
  .hanger--front{left:97px}
  .hanger--back{left:575px}
  .door-hole{position:absolute;left:71px;top:39px;width:266px;height:215px;background:var(--stage);border-radius:133px 133px 0 0/110px 110px 0 0;box-shadow:inset 0 4px 8px rgba(0,0,0,.3)}
  .bands{position:absolute;inset:0;width:409px;height:1057px}
  .photo{position:absolute;inset:0}
  .photo--front{clip-path:polygon(0 481px,204px 418px,409px 481px,409px 770px,204px 707px,0 770px);
    background:linear-gradient(120deg,#8d6a3e 0%,#c9a874 22%,#e0d3b4 42%,#f3f1ec 52%,#ffffff 70%,#e6e6e6 100%)}
  .photo--back{clip-path:polygon(0 615px,204px 555px,409px 615px,409px 770px,204px 707px,0 770px);
    background:linear-gradient(180deg,#bdb8b0 0%,#d8d4cc 35%,#f1efea 60%,#8a857c 80%,#5a4636 100%)}
  .license{position:absolute;top:20px;right:27px;font-weight:700;font-size:13.5px}
  .badges{position:absolute;top:18px;left:27px;display:flex;gap:8px;align-items:center}
  .badge{width:22px;height:20px;background:var(--ink)}
  .badge--round{border-radius:50%;width:22px;height:22px}
  .badge--light{background:#e9e9e9}
  .center{position:absolute;left:0;width:409px;text-align:center}
  .intro{top:279px;font-weight:700;font-size:14.5px;line-height:17px;text-transform:uppercase}
  .headline{top:313px;font-family:"Bebas Neue",sans-serif;font-size:47px;line-height:47px;letter-spacing:1px}
  .subline{top:360px;font-weight:700;font-size:11.6px;text-transform:uppercase}
  .pill{position:absolute;border-radius:20px;font-weight:700;text-align:center;text-transform:uppercase;white-space:nowrap}
  .pill--dark{left:80px;top:380px;width:248px;height:18px;line-height:18px;background:var(--ink);font-size:11.5px}
  .steps-title{top:275px;font-family:"Bebas Neue",sans-serif;font-size:57px;line-height:56px;letter-spacing:2px}
  .step-icon{position:absolute;top:400px;width:70px;height:70px;border-radius:50%;background:var(--ink);border:2px solid var(--white)}
  .step-icon svg{position:absolute;left:17px;top:17px;width:32px;height:32px}
  .step-arrow{position:absolute;top:429px;width:34px;height:12px}
  .step-label{position:absolute;top:478px;width:120px;text-align:center;font-size:14.5px;line-height:16px}
  .brand{top:822px;font-family:"Tinos",serif;font-weight:400;font-size:19px;letter-spacing:1px;color:var(--white)}
  .pill--blue{background:var(--blue);color:var(--white);font-size:13px;height:17px;line-height:17px}
  .services{top:881px;font-size:12px;line-height:17px}
  .sep{color:var(--blue);padding:0 4px}
  .selling{top:852px;color:var(--blue);font-size:23.5px;text-transform:uppercase}
  .offer{top:908px;font-size:14.5px}
  .phone-band{position:absolute;left:0;top:952px;width:409px;height:72px;background:var(--blue)}
  .pill--call{left:119px;top:944px;width:170px;height:17px;line-height:17px;background:var(--white);color:var(--ink);font-size:13.5px}
  .phone{top:961px;font-weight:700;font-size:62px;line-height:62px;letter-spacing:-1.5px}
  .footer{position:absolute;left:0;top:1024px;width:409px;height:33px;background:var(--ink);text-align:center;line-height:33px;font-size:11.5px;letter-spacing:3.4px}
</style>
</head>
<body>
<main class="stage">

  <section class="hanger hanger--front">
    <svg class="bands" viewBox="0 0 409 1057" aria-hidden="true">
      <polygon points="0,464 204,405 409,464 409,481 204,418 0,481" fill="#141414"/>
      <line x1="0" y1="452" x2="150" y2="410" stroke="#fff" stroke-width="4"/>
      <line x1="262" y1="410" x2="409" y2="452" stroke="#fff" stroke-width="4"/>
      <polygon points="0,782 204,722 409,782 409,1057 0,1057" fill="#141414"/>
      <line x1="0" y1="796" x2="150" y2="753" stroke="#fff" stroke-width="4"/>
      <line x1="262" y1="753" x2="409" y2="796" stroke="#fff" stroke-width="4"/>
    </svg>
    <div class="photo photo--front" role="img" aria-label="Finished kitchen with white cabinets and granite counters blending into a line drawing of the same kitchen"></div>
    <div class="door-hole"></div>
    <p class="license">CSLB# 4820516</p>
    <p class="center intro">Your Neighbor Just Remodeled<br>Come See Our Work At</p>
    <h1 class="center headline">LOVE YOUR HOME AGAIN!</h1>
    <p class="center subline">We Make Remodeling Easy &nbsp;|&nbsp; Free 3D Design Services</p>
    <p class="pill pill--dark">★ &nbsp;Licensed General Contractors&nbsp; ★</p>
    <p class="center brand">HEARTHWELL BUILDERS</p>
    <p class="pill pill--blue" style="left:131px;top:859px;width:146px">We Specialize In</p>
    <p class="center services">
      Kitchen Remodel<span class="sep">|</span>Bathroom Remodel<span class="sep">|</span>Water and Mold Damage<br>
      Interior/Exterior Painting<span class="sep">|</span>Energy Efficient Upgrades<br>
      Flooring: Carpet, Vinyl, Wood and Tile<span class="sep">|</span>Window/Door Replacement
    </p>
    <div class="phone-band"></div>
    <p class="pill pill--call">Call or Text Now!</p>
    <p class="center phone">858-555-0147</p>
    <p class="footer">www.OakvaleHomeworks.example</p>
  </section>

  <section class="hanger hanger--back">
    <svg class="bands" viewBox="0 0 409 1057" aria-hidden="true">
      <polygon points="0,603 204,542 409,603 409,615 204,555 0,615" fill="#141414"/>
      <line x1="0" y1="591" x2="150" y2="548" stroke="#fff" stroke-width="4"/>
      <line x1="262" y1="548" x2="409" y2="591" stroke="#fff" stroke-width="4"/>
      <polygon points="0,782 204,722 409,782 409,1057 0,1057" fill="#141414"/>
      <line x1="0" y1="796" x2="150" y2="753" stroke="#fff" stroke-width="4"/>
      <line x1="262" y1="753" x2="409" y2="796" stroke="#fff" stroke-width="4"/>
    </svg>
    <div class="photo photo--back" role="img" aria-label="Remodeled grey kitchen with white island, pendant lights and wood floor"></div>
    <div class="door-hole"></div>
    <div class="badges" aria-hidden="true">
      <span class="badge"></span>
      <span class="badge badge--light"></span>
      <span class="badge badge--round"></span>
    </div>
    <p class="license">CSLB# 4820516</p>
    <h2 class="center steps-title">GET STARTED<br>IN 3 SIMPLE STEPS</h2>

    <div class="step-icon" style="left:32px">
      <svg viewBox="0 0 32 32" fill="none" stroke="#fff" stroke-width="2"><rect x="3" y="5" width="26" height="17" rx="1"/><line x1="16" y1="22" x2="16" y2="27"/><line x1="10" y1="27" x2="22" y2="27"/><line x1="8" y1="12" x2="24" y2="12"/><line x1="8" y1="16" x2="20" y2="16"/></svg>
    </div>
    <svg class="step-arrow" style="left:116px" viewBox="0 0 34 12" aria-hidden="true"><line x1="0" y1="6" x2="31" y2="6" stroke="#fff" stroke-width="1.6"/><polyline points="25,1 32,6 25,11" fill="none" stroke="#fff" stroke-width="1.6"/></svg>
    <div class="step-icon" style="left:164px">
      <svg viewBox="0 0 32 32" fill="none" stroke="#fff" stroke-width="2"><rect x="6" y="5" width="20" height="24" rx="1"/><rect x="12" y="2" width="8" height="5" fill="#fff"/><path d="M16 11 l5 2 v4 c0 3-2 5-5 6 c-3-1-5-3-5-6 v-4z"/><polyline points="13.5,17 15.5,19 19,15"/></svg>
    </div>
    <svg class="step-arrow" style="left:248px" viewBox="0 0 34 12" aria-hidden="true"><line x1="0" y1="6" x2="31" y2="6" stroke="#fff" stroke-width="1.6"/><polyline points="25,1 32,6 25,11" fill="none" stroke="#fff" stroke-width="1.6"/></svg>
    <div class="step-icon" style="left:295px">
      <svg viewBox="0 0 32 32"><path d="M16 4 L2 16 H6 V28 H13 V20 H19 V28 H26 V16 H30 Z" fill="#fff"/></svg>
    </div>

    <p class="step-label" style="left:7px">Order<br>Free Estimate<br>And Design</p>
    <p class="step-label" style="left:139px">Approve<br>Estimate<br>And Design</p>
    <p class="step-label" style="left:265px;width:130px">Hearthwell<br>Builders Builds<br>Your Dream</p>

    <p class="center brand" style="top:818px">HEARTHWELL BUILDERS</p>
    <p class="center selling">Thinking About Selling?</p>
    <p class="pill pill--blue" style="left:143px;top:886px;width:124px">We Buy Home</p>
    <p class="center offer">Get Cash Offer &nbsp;|&nbsp; Selling Made Easy</p>
    <div class="phone-band"></div>
    <p class="pill pill--call">Call or Text Now!</p>
    <p class="center phone">858-555-0147</p>
    <p class="footer">www.OakvaleHomeworks.example</p>
  </section>

</main>
</body>
</html>
```